Cedarline Residences —-

Letter head for my apartment building of 15 Floors
In Kampala, Uganda

CEDARLINE RESIDENCIES
14 KIVARA RIDGE ROAD
NAGURU - KAMPALA
P.O. BOX 38516
KAMPALA— UGANDA

```html
<!DOCTYPE html>
<html lang="en">
<head>
<meta charset="utf-8">
<title>Cedarline Residences — Letterhead</title>
<link rel="stylesheet" href="https://fonts.googleapis.com/css2?family=Arimo:wght@400&display=swap">
<style>
  :root {
    --backdrop: #dedede;
    --paper: #ffffff;
    --paper-shade: #eeeeee;
    --brand-blue: #1d5289;
    --ink: #4a4a4a;
    --ink-soft: #555555;
    --rule: #8a8a8a;
    --signature-tone: #dcdcdc;
  }
  * { box-sizing: border-box; margin: 0; padding: 0; }
  html, body {
    width: 1200px; height: 1141px; overflow: hidden;
    background: var(--backdrop);
  }
  .letterhead {
    position: absolute; left: 194px; top: 0;
    width: 812px; height: 1141px;
    background: linear-gradient(135deg, var(--paper) 45%, var(--paper-shade) 100%);
    font-family: "Arimo", Arial, sans-serif;
    color: var(--ink);
  }
  .brand {
    position: absolute; left: 61px; top: 100px;
    font-family: "Arimo", Arial, sans-serif;
    font-weight: 400; font-size: 24px; line-height: 30px;
    color: var(--brand-blue); letter-spacing: 1px; white-space: nowrap;
  }
  .address {
    position: absolute; left: 621px; top: 84px; height: 62px;
    border-left: 1px solid var(--rule); padding-left: 12px;
    font-style: normal;
    font-size: 12.5px; line-height: 15.5px; color: var(--ink-soft);
  }
  .address p + p { margin-top: 4px; }
  .letter { position: absolute; left: 61px; top: 284px; width: 693px; }
  .salutation { font-size: 19px; line-height: 24px; color: var(--ink-soft); margin-bottom: 32px; }
  .body-copy p {
    font-size: 11.5px; line-height: 17.2px; text-align: justify;
    margin-bottom: 17px; color: var(--ink);
  }
  .closing { font-size: 11.6px; margin-top: 33px; }
  .signature {
    position: absolute; left: 56px; top: 772px; width: 234px; height: 58px;
    background: radial-gradient(ellipse at 45% 55%, var(--signature-tone) 0%, rgba(220,220,220,0) 70%);
  }
  .footer-band {
    position: absolute; left: 0; bottom: 0; width: 100%; height: 11px;
    background: var(--brand-blue);
  }
</style>
</head>
<body>
  <main class="letterhead">
    <header>
      <div class="brand">CEDARLINE RESIDENCIES</div>
      <address class="address">
        <p>14 Kivara Ridge Road<br>Naguru - Kampala</p>
        <p>P.O. BOX 38516<br>Kampala - Uganda</p>
      </address>
    </header>

    <section class="letter">
      <p class="salutation">Dear Mr. Halden,</p>
      <div class="body-copy">
        <p>Lorem ipsum dolor sit amet, consectetur adipiscing elit. Donec orci purus, luctus vitae dignissim eu, iaculis sed purus. Vivamus faucibus, ipsum nec aliquet viverra, leo mauris condimentum ligula, sit amet sagittis enim ligula quis arcu. Nam egestas tortor id nisi porttitor mattis. In tortor ante, ultricies in suscipit a, tempus non massa. Vivamus et auctor mi. Fusce vel massa nulla. Phasellus nec eros mauris, et scelerisque orci.</p>
        <p>Donec malesuada orci vitae nulla accumsan porta a id massa. Quisque accumsan iaculis magna sit amet fringilla. Maecenas consequat, magna eget tincidunt semper, odio nibh rutrum mi, id feugiat ante nisi eu risus. Vestibulum nunc orci, rhoncus a placerat in, ultricies in mi. Cras mattis varius eros, vel fringilla nisi suscipit eget. Quisque scelerisque sagittis nulla at porttitor.</p>
        <p>Sed id augue vitae urna euismod commodo aliquet a quam. Pellentesque arcu velit, cursus et malesuada ut, consequat et diam. Nullam erat sem, rhoncus id ullamcorper vitae, rhoncus et arcu. In ultricies ultricies nulla, ut rutrum nisi iaculis at. Donec eu magna a metus ornare faucibus. Fusce aliquet faucibus ultricies. Morbi semper, est id tincidunt gravida, sem arcu adipiscing lacus, ac bibendum nulla leo eu purus. Quisque nec diam sed risus consectetur a ccumsan quis quis nibh. Vestibulum id purus lorem.</p>
        <p>It is a long established fact that a reader will be distracted by the readable content of a page when looking at its layout. The point of using Lorem Ipsum is that it has a more-or-less normal distribution of letters, as opposed to using 'Content here, content here', making it look like readable English. Many desktop publishing packages</p>
        <p>ada ut, consequat et diam. Nullam erat sem, rhoncus id ullamcorper vitae, rhoncus et arcu. In ultricies ultricies nulla, ut rutrum nisi iaculis at. Donec eu magna a metus ornare faucibus. Fusce aliquet faucibus ultricies. Morbi semper,</p>
      </div>
      <p class="closing">Sincerely,</p>
    </section>

    <div class="signature" role="img" aria-label="Handwritten signature of the sender"></div>
    <div class="footer-band"></div>
  </main>
</body>
</html>
```